Kelvane Electric short form flyer brochure

need a new brochure short form flyer to give to customers to highlight our capabilities,
we are merging 3 companies into one,
Kelvane Electric, Kelvane Forgeline, Kelvane Specialised portable buildings,
want to show case electrical Sheetmetal and building capabilities all on one bi fold out brochure, total 8 sided folded into A4,
pages as follows,
kelvane logo,
company profile,
electrical capabilities
electrical photos
Sheetmetal capabilities
sheet metal products
transportable buildings capabilities
range of other products.

will provide photos, most information will be on the web page,
www.kelvaneelectric.example.au

design needs to be fresh modern
any suggestions and tips will be welcomed

Target Market(s)

Utilities, power and water sectors, manufacturing

Requirements
Must have
• modern fresh design, bi fold into A4, total 8 sides design
Nice to have
• hints and tips to make it better, ask for information and photos if required

```html
<!DOCTYPE html>
<html lang="en">
<head>
<meta charset="utf-8">
<title>Kelvane Electric – Bi-fold Brochure Covers</title>
<link href="https://fonts.googleapis.com/css2?family=Anton&family=Archivo:wght@800&family=Roboto:wght@400;700;900&display=swap" rel="stylesheet">
<style>
  :root {
    --red: #e8262d;
    --blue: #1f3f8c;
    --white: #ffffff;
    --paper: #f4f4f5;
    --ink: #2b2b2b;
    --stage: #e6e7ea;
    --sky: #c9d9e6;
    --gravel: #8c8c88;
  }
  * { box-sizing: border-box; margin: 0; padding: 0; }
  html, body { width: 1200px; height: 900px; overflow: hidden; }
  body { background: var(--stage); font-family: "Roboto", Arial, sans-serif; }

  .spread {
    position: absolute; left: 80px; top: 82px;
    width: 1040px; height: 736px;
    display: flex;
    box-shadow: 0 10px 30px rgba(0,0,0,.18);
  }
  .page { position: relative; width: 520px; height: 736px; overflow: hidden; }
  .page svg.art { position: absolute; inset: 0; width: 100%; height: 100%; }

  /* Back cover */
  .back { background: linear-gradient(160deg, var(--white) 0%, var(--paper) 60%, #e4e4e6 100%); }
  .contact { position: absolute; left: 120px; top: 112px; width: 300px; text-align: center; }
  .contact__group { color: var(--red); font: 900 17px "Roboto", Arial, sans-serif; }
  .contact__group span { color: var(--blue); }
  .contact__address { color: var(--ink); font-size: 13px; line-height: 1.25; margin-top: 4px; }
  .contact__lines { margin-top: 10px; text-align: left; padding-left: 20px; }
  .contact__row { display: flex; align-items: center; gap: 14px; height: 24px; }
  .contact__icon { width: 20px; height: 16px; border-radius: 3px; background: var(--red); display: flex; align-items: center; justify-content: center; }
  .contact__phone { color: var(--blue); font: 900 16px "Roboto", Arial, sans-serif; }
  .contact__email { color: var(--ink); font-size: 12px; }

  .clients__title { position: absolute; left: 0; width: 540px; text-align: center; top: 268px; color: var(--red); font: 900 18px "Roboto", Arial, sans-serif; }
  .clients__title span { color: var(--blue); }
  .clients { position: absolute; left: 110px; top: 298px; width: 320px; display: grid; grid-template-columns: repeat(3, 1fr); gap: 7px 10px; }
  .client { color: var(--blue); font: 700 11px/13px "Roboto", Arial, sans-serif; white-space: nowrap; }

  /* Front cover */
  .front { background: var(--blue); }
  .headline { position: absolute; left: 0; right: 0; top: 88px; text-align: center; }
  .headline__main { color: var(--white); font: 400 50px/1 "Anton", Impact, sans-serif; letter-spacing: 1px; }
  .headline__sub { color: var(--blue); font: 800 21px/1 "Archivo", Arial, sans-serif; letter-spacing: 1.5px; margin-top: 4px; }
  .brand { position: absolute; left: 304px; top: 470px; width: 196px; height: 196px; border-radius: 50%; display: flex; align-items: center; justify-content: center; }
  .brand__name { color: var(--blue); font: 900 34px "Roboto", Arial, sans-serif; }
</style>
</head>
<body>
<main class="spread">

  <!-- Back cover -->
  <section class="page back">
    <svg class="art" viewBox="0 0 520 736">
      <defs>
        <clipPath id="back-photo-clip"><circle cx="95" cy="650" r="118"/></clipPath>
        <linearGradient id="unit-grad" x1="0" y1="0" x2="0" y2="1">
          <stop offset="0" stop-color="#d9d6cf"/><stop offset="1" stop-color="#b9b4aa"/>
        </linearGradient>
      </defs>
      <path d="M0 600 C 150 520, 320 470, 520 330 L520 736 L0 736 Z" fill="var(--red)"/>
      <path d="M0 618 C 160 538, 330 488, 520 352 L520 736 L0 736 Z" fill="var(--white)"/>
      <path d="M0 632 C 165 552, 340 502, 520 366 L520 736 L0 736 Z" fill="var(--blue)"/>
      <circle cx="95" cy="650" r="142" fill="var(--red)"/>
      <circle cx="95" cy="650" r="132" fill="var(--white)"/>
      <circle cx="95" cy="650" r="124" fill="var(--blue)"/>
      <g role="img" aria-label="Photo of a cream electrical switchgear kiosk">
        <rect x="-30" y="530" width="250" height="240" fill="url(#unit-grad)" clip-path="url(#back-photo-clip)"/>
      </g>
    </svg>

    <div class="contact">
      <p class="contact__group">KELVANE <span>GROUP</span></p>
      <p class="contact__address">48-56 Calloway Drive Hallam North,<br>VIC 3180 Australia</p>
      <div class="contact__lines">
        <div class="contact__row">
          <span class="contact__icon"><svg width="10" height="10" viewBox="0 0 10 10"><path d="M2 1 L4 1 L4.6 3 L3.4 3.8 Q4.5 6 6.2 6.6 L7 5.4 L9 6 L9 8 Q5 9 2 5 Q1 3 2 1Z" fill="#fff"/></svg></span>
          <span class="contact__phone">+61 (0)3 9000 4182</span>
        </div>
        <div class="contact__row">
          <span class="contact__icon"><svg width="12" height="10" viewBox="0 0 12 10"><rect x="1" y="3" width="10" height="6" rx="1" fill="#fff"/><rect x="3" y="0.5" width="6" height="3" fill="#fff"/></svg></span>
          <span class="contact__phone">+61 (0)3 9000 4197</span>
        </div>
        <div class="contact__row">
          <span class="contact__icon"><svg width="12" height="9" viewBox="0 0 12 9"><rect x="0.5" y="0.5" width="11" height="8" fill="#fff"/><path d="M0.5 0.5 L6 5 L11.5 0.5" stroke="var(--red)" fill="none"/></svg></span>
          <span class="contact__email">info@kelvaneelectric.example.au</span>
        </div>
      </div>
    </div>

    <p class="clients__title">OUR <span>CLIENTS</span></p>
    <div class="clients">
      <span class="client">Tharrow</span>
      <span class="client">Elmsbury</span>
      <span class="client">Sierholt</span>
      <span class="client">Wendale</span>
      <span class="client">Voltacor</span>
      <span class="client">Brell</span>
      <span class="client">Linegrid</span>
      <span class="client">Southnet</span>
      <span class="client">Ramwell</span>
      <span class="client">Corvio</span>
      <span class="client">Jarrah Energy</span>
      <span class="client">Apex Pipe Group</span>
      <span class="client">Marlin Fuels</span>
    </div>
  </section>

  <!-- Front cover -->
  <section class="page front">
    <svg class="art" viewBox="0 0 520 736">
      <defs>
        <clipPath id="front-photo-clip"><ellipse cx="250" cy="455" rx="290" ry="160"/></clipPath>
        <linearGradient id="site-grad" x1="0" y1="0" x2="0" y2="1">
          <stop offset="0" stop-color="var(--sky)"/>
          <stop offset="0.45" stop-color="#e1e3e2"/>
          <stop offset="0.6" stop-color="#b8b6b0"/>
          <stop offset="1" stop-color="var(--gravel)"/>
        </linearGradient>
      </defs>
      <path d="M0 0 H520 V250 C 380 250, 200 300, 0 330 Z" fill="var(--red)"/>
      <path d="M0 330 C 200 300, 380 250, 520 250" stroke="var(--white)" stroke-width="8" fill="none"/>
      <ellipse cx="250" cy="455" rx="290" ry="160" fill="var(--white)"/>
      <g role="img" aria-label="Photo of transportable electrical switch rooms on a gravel site">
        <rect x="-50" y="290" width="600" height="330" fill="url(#site-grad)" clip-path="url(#front-photo-clip)"/>
      </g>
      <ellipse cx="250" cy="455" rx="282" ry="152" fill="none" stroke="var(--white)" stroke-width="6"/>
      <circle cx="402" cy="568" r="108" fill="var(--white)"/>
      <circle cx="402" cy="568" r="100" fill="none" stroke="var(--red)" stroke-width="4"/>
    </svg>

    <header class="headline">
      <h1 class="headline__main">A LEADERSHIP OF</h1>
      <p class="headline__sub">TOTAL ELECTRIC SOLUTION</p>
    </header>

    <div class="brand"><span class="brand__name">Kelvane</span></div>
  </section>

</main>
</body>
</html>
```